Business Card Design Project

Use our current logo. Clean design.

Industry/Entity Type

Business

Requirements
Must have
• Marisela DUBRANCQ
M. Law
Managing Partner

Alpenvorsa AG
Kornhalmweg 214
CH-3097 Liebefeld

M. +41 79 412 56 27
T. +41 31 928 44 10
F. +41 31 928 44 19

m.dubrancq@alpenvorsa-example.com
www.alpenvorsa-example.com

```html
<!DOCTYPE html>
<html lang="de">
<head>
<meta charset="utf-8">
<title>Alpenvorsa AG – Visitenkarte</title>
<link rel="stylesheet" href="https://fonts.googleapis.com/css2?family=Lato:wght@400;700&display=swap">
<style>
  :root {
    --stage: #e6e6e6;
    --brand-red: #e8000d;
    --brand-red-deep: #c4000a;
    --paper: #ffffff;
    --paper-shade: #f1f1f1;
    --ink: #1f1b1c;
    --ink-soft: #3a3a3a;
    --font-text: "Lato", "Helvetica Neue", Arial, sans-serif;
  }
  * { box-sizing: border-box; margin: 0; padding: 0; }
  html, body {
    width: 1200px; height: 900px; overflow: hidden;
    background: var(--stage);
    font-family: var(--font-text);
  }
  .canvas {
    width: 1200px; height: 900px;
    display: flex; flex-direction: column;
    align-items: center; justify-content: center; gap: 40px;
  }
  .card {
    position: relative;
    width: 640px; height: 376px;
    box-shadow: 0 10px 28px rgba(0,0,0,0.18);
    overflow: hidden;
  }

  /* Front side */
  .card--front {
    background: linear-gradient(135deg, var(--brand-red) 0%, var(--brand-red-deep) 100%);
    display: flex; align-items: center; justify-content: center;
  }
  .wordmark {
    font-family: var(--font-text);
    font-weight: 400;
    letter-spacing: 0.08em;
    text-transform: uppercase;
    white-space: nowrap;
  }
  .card--front .wordmark { color: var(--paper); font-size: 46px; }

  /* Back side */
  .card--back {
    background: linear-gradient(160deg, var(--paper) 0%, var(--paper-shade) 100%);
  }
  .card--back .wordmark {
    position: absolute; left: 44px; top: 150px;
    color: var(--ink); font-size: 30px;
  }
  .contact {
    position: absolute; left: 372px; top: 46px;
    color: var(--ink-soft);
    font-size: 13.5px; line-height: 1.3;
  }
  .contact__name { color: var(--brand-red); font-size: 19px; font-weight: 400; margin-bottom: 4px; }
  .contact__role { color: var(--ink); font-size: 11.5px; font-weight: 700; line-height: 1.25; margin-bottom: 14px; }
  .contact__phones { list-style: none; margin-bottom: 22px; }
  .contact__phones li { display: flex; gap: 10px; }
  .contact__label { color: var(--brand-red); width: 12px; }
  .contact__address { font-style: normal; margin-bottom: 20px; }
  .contact__email { color: var(--ink-soft); }
  .contact__web { color: var(--brand-red); }
  .card__band {
    position: absolute; left: 0; right: 0; bottom: 0; height: 16px;
    background: linear-gradient(90deg, var(--brand-red-deep), var(--brand-red));
  }
</style>
</head>
<body>
  <main class="canvas">
    <section class="card card--front" aria-label="Vorderseite">
      <span class="wordmark">Alpenvorsa</span>
    </section>

    <section class="card card--back" aria-label="Rückseite">
      <span class="wordmark">Alpenvorsa</span>
      <div class="contact">
        <h1 class="contact__name">Marisela DUBRANCQ</h1>
        <p class="contact__role">M. Law<br>Managing Partner</p>
        <ul class="contact__phones">
          <li><span class="contact__label">M</span>+41 79 412 56 27</li>
          <li><span class="contact__label">T</span>+41 31 928 44 10</li>
          <li><span class="contact__label">F</span>+41 31 928 44 19</li>
        </ul>
        <address class="contact__address">
          Alpenvorsa AG<br>
          Kornhalmweg 214<br>
          CH-3097 Liebefeld
        </address>
        <p class="contact__email">m.dubrancq@alpenvorsa-example.com</p>
        <p class="contact__web">www.alpenvorsa-example.com</p>
      </div>
      <div class="card__band"></div>
    </section>
  </main>
</body>
</html>
```